Business card design needed

am looking for a fun and funky design to match our moto, seriously fun swimwear and fashion for girls.

We manufacture and retail girls swimwear and fashion in Australia. Our designs are fun loving and funky. I would like to use bright fuschia to match our website www.breezyplum.com.au. We target a higher end market so need it to reflect this.

Industry/Entity Type

Fashion

Contact Information for Business Card

Breezy Plum logo,
Maddie Lorne
(07) 35517204
admin@breezyplum.com.au
www.breezyplum.com.au

Logo Text

Breezy Plum

```html
<!DOCTYPE html>
<html lang="en">
<head>
<meta charset="utf-8">
<title>Breezy Plum – Business Card</title>
<link rel="stylesheet" href="https://fonts.googleapis.com/css2?family=Barlow+Semi+Condensed:wght@300;400&display=swap">
<style>
  :root {
    --fuchsia: #e41ad6;
    --fuchsia-deep: #c915bd;
    --card-white: #fbfbfb;
    --backdrop: #ffffff;
    --text-light: #ffffff;
    --shadow: rgba(0, 0, 0, 0.12);
  }

  * { box-sizing: border-box; margin: 0; padding: 0; }

  html, body {
    width: 1200px;
    height: 900px;
    overflow: hidden;
    background: var(--backdrop);
  }

  .canvas {
    position: relative;
    width: 1200px;
    height: 900px;
  }

  .business-card {
    position: absolute;
    left: 145px;
    top: 190px;
    width: 910px;
    height: 520px;
    background: var(--fuchsia);
    overflow: hidden;
    box-shadow: 0 14px 40px var(--shadow);
  }

  .card-shapes {
    position: absolute;
    inset: 0;
    width: 100%;
    height: 100%;
  }

  .logo-wordmark {
    position: absolute;
    left: 40px;
    top: 225px;
    width: 400px;
    text-align: center;
    font-family: "Barlow Semi Condensed", sans-serif;
    font-weight: 400;
    font-size: 66px;
    letter-spacing: 1px;
    color: var(--fuchsia);
  }

  .contact-block {
    position: absolute;
    left: 560px;
    top: 125px;
    font-family: "Barlow Semi Condensed", sans-serif;
    font-weight: 300;
    color: var(--text-light);
    line-height: 1.25;
  }

  .contact-name {
    font-size: 40px;
    font-weight: 400;
    letter-spacing: 0.5px;
    margin-bottom: 4px;
  }

  .contact-line {
    font-size: 28px;
    letter-spacing: 0.3px;
  }
</style>
</head>
<body>
  <main class="canvas">
    <section class="business-card" aria-label="Breezy Plum business card">
      <svg class="card-shapes" viewBox="0 0 910 520" aria-hidden="false">
        <g role="img" aria-label="Faint spiral decoration in deeper fuchsia">
          <circle cx="640" cy="235" r="230" fill="var(--fuchsia-deep)" opacity="0.35"/>
        </g>
        <path class="white-panel" d="M0 0 H470 C520 150 470 380 300 520 H0 Z" fill="var(--card-white)"/>
      </svg>

      <div class="logo-wordmark">Breezy Plum</div>

      <div class="contact-block">
        <p class="contact-name">Maddie Lorne</p>
        <p class="contact-line">(07) 35517204</p>
        <p class="contact-line">admin@breezyplum.com.au</p>
        <p class="contact-line">www.breezyplum.com.au</p>
      </div>
    </section>
  </main>
</body>
</html>
```